TORV graphic design elements

TORV is a group of schools who have adopted positive psychology as the framework for their wellbeing programs.

Designs should be simple and formal (rather than ultra modern/trendy)

I require quotes for the following:
Letterhead
Business Card
Powerpoint slides
Pull up banner (approx 2m high)
Colour pallette development

I have uploaded a copy of our logo

```html
<!DOCTYPE html>
<html lang="en">
<head>
<meta charset="utf-8">
<title>Stationery: Staff Letterhead</title>
<link rel="stylesheet" href="https://fonts.googleapis.com/css2?family=Carlito:wght@400;700&family=Source+Sans+3:wght@300;400;600&display=swap">
<style>
  :root {
    --brand-purple: #4b2a86;
    --ink: #1c1c1c;
    --muted: #555555;
    --rule: #a9a9a9;
    --frame: #8a8a8a;
    --paper: #ffffff;
    --mark-red: #e3262e;
  }
  * { margin: 0; padding: 0; box-sizing: border-box; }
  html, body { width: 1200px; height: 1101px; overflow: hidden; background: var(--paper); }
  .sheet { position: relative; width: 1200px; height: 1101px; font-family: "Source Sans 3", Arial, sans-serif; color: var(--ink); }

  .sheet-title { position: absolute; left: 38px; top: 14px; font-size: 50px; font-weight: 300; color: var(--brand-purple); letter-spacing: -0.3px; }

  .letter { position: absolute; left: 31px; top: 99px; width: 738px; height: 956px; border: 1px solid var(--frame); background: var(--paper); font-family: "Carlito", "Calibri", sans-serif; font-size: 12.6px; color: var(--ink); }
  .brand { position: absolute; left: 0; width: 100%; top: 46px; display: flex; justify-content: center; align-items: center; gap: 10px; }
  .brand-dot { width: 26px; height: 26px; border-radius: 50%; background: var(--mark-red); }
  .brand-name { font-size: 44px; font-weight: 700; color: var(--mark-red); line-height: 1; letter-spacing: 1px; }
  .brand-rule { position: absolute; left: 86px; top: 100px; width: 556px; height: 1px; background: var(--rule); }
  .brand-tagline { position: absolute; left: 0; width: 100%; top: 104px; text-align: center; font-size: 11.5px; color: var(--muted); letter-spacing: 0.6px; padding-left: 40px; }

  .letter-date, .recipient, .salutation, .body-para, .role-list, .signature { position: absolute; left: 86px; width: 560px; }
  .letter-date { top: 213px; }
  .recipient { top: 265px; line-height: 16px; }
  .salutation { top: 398px; }
  .body-para { line-height: 14px; }
  .para-one { top: 425px; }
  .para-two { top: 538px; }
  .role-list { top: 585px; list-style: none; line-height: 16px; }
  .role-list li:nth-child(1) { padding-left: 14px; }
  .role-list li:nth-child(2) { padding-left: 14px; }
  .role-list li:nth-child(3) { text-indent: 14px; }
  .signature { top: 724px; }

  .letter-footer { position: absolute; left: 0; width: 100%; top: 880px; text-align: center; font-size: 11.6px; line-height: 13.5px; color: #333; padding-left: 50px; }

  .spec { position: absolute; left: 810px; top: 90px; width: 380px; }
  .spec-title { font-size: 38px; font-weight: 300; color: var(--brand-purple); line-height: 46px; }
  .spec-heading { margin-top: 24px; font-size: 20px; font-weight: 600; color: #222; }
  .margin-list { list-style: none; font-size: 21px; font-weight: 300; color: #222; line-height: 24.5px; }
  .spec-note { margin-top: 14px; font-size: 13.4px; color: #222; line-height: 17px; width: 380px; }
</style>
</head>
<body>
<div class="sheet">
  <h1 class="sheet-title">Stationery: Staff Letterhead</h1>

  <div class="letter">
    <div class="brand"><span class="brand-dot"></span><span class="brand-name">TORV</span></div>
    <div class="brand-rule"></div>
    <p class="brand-tagline">Teaching Optimism, Resilience &amp; Values</p>

    <p class="letter-date">Juin 2th, 2013</p>
    <p class="recipient">Mr. Daniel Hartley<br>Title<br>Company<br>245 street<br>Suite 230<br>City (Province)</p>
    <p class="salutation">Sir,</p>
    <p class="body-para para-one">he Wellbeing Practice Board (WPB) has announced that there will be an extension of the date by which supervisors of trainee psychologists are required to have completed the new mandatory supervisor training requirements. The WPB has extended the transition arrangements for completion of mandatory supervisor training to the new deadline of 30 June 2018, but supervisors must be on the WPB’s list of approved supervisors by 30 June 2013 for this to be applicable.</p>
    <p class="body-para para-two">The WPB’s mandatory supervisor training requirements to enable approved supervisor status apply to psychologists providing supervision to:</p>
    <ul class="role-list">
      <li>Provisional psychologists undertaking a 4+2 internship program or a 5+1 internship program</li>
      <li>Postgraduate students undertaking placements as part of an ACWE accredited professional psychology training program</li>
      <li>Psychologists undertaking a registrar program leading to endorsement in an approved area of practice.</li>
    </ul>
    <p class="signature">Daniel Hartley</p>

    <p class="letter-footer">Northbridge Wellbeing Council<br>18 Harlow Lane, Kirrawee NSW 2232, Australia<br>T. +61 2 5550 1834 &nbsp;&nbsp; F. 5550 1835 &nbsp;&nbsp; www.torv.com</p>
  </div>

  <aside class="spec">
    <h2 class="spec-title">Stationery:<br>Staff Letterhead</h2>
    <h3 class="spec-heading">Margins:</h3>
    <ul class="margin-list">
      <li>Left: 24 mm</li>
      <li>Right:24 mm</li>
      <li>Top: 15 mm</li>
      <li>Bottom: 12 mm</li>
    </ul>
    <p class="spec-note">The logo is in the top center and is set in Segoe UI Symbol on 8.5 pts.</p>
    <p class="spec-note">The address information at the bottem center of the page is set in Segoe UI Symbol 9 pts</p>
    <p class="spec-note">Size 21x29.7 cm</p>
  </aside>
</div>
</body>
</html>
```